Brochure required for international Sports event

We need an 8 page brochure designed for an international sports event to be hosted in Japan. We are a Travel Company providing packages for participants looking to travel to the event.
The brochure will feature information on the event as well as services our company can provide.
The Brochure is to be an 8 page A4 document in portrait layout.
The brochure needs to be provided both as a print ready document and digital brochure for emailing.
Brochure structure, copy, logo and imagery has been provided
As well as a example brochure design that we like for inspiration.
Link to icons - https://www.filevault-example.net/sh/kq3mzplr8wbtyoc/BBBxkTLmQ4pR7Hs2nW6vYbCgE?dl=0
Target Market(s)
Masters/Veterans Sports Participants
Industry/Entity Type
Travel
Colors
Designer to choose colors to be used in the design.
Look and feel
Each slider illustrates characteristics of the customer's brand and the style your logo design should communicate.

```html
<!DOCTYPE html>
<html lang="en">
<head>
<meta charset="utf-8">
<title>Global Veterans Games 2021 – Brochure Spreads</title>
<link href="https://fonts.googleapis.com/css2?family=Oswald:wght@500;600&family=Roboto:wght@500;700&family=Montserrat:wght@300;400;500;600;700&display=swap" rel="stylesheet">
<style>
  :root{
    --bg:#ececec;
    --paper:#ffffff;
    --orange:#f0961f;
    --ink:#3d3d3d;
    --charcoal:#454545;
    --panel:#4c4c4c;
    --body:#444444;
  }
  *{box-sizing:border-box;margin:0;padding:0}
  html,body{width:1200px;height:1200px;overflow:hidden;background:var(--bg);font-family:"Montserrat",sans-serif}
  .canvas{position:relative;width:1200px;height:1200px}
  .page{position:absolute;width:354px;height:501px;background:var(--paper);overflow:hidden;box-shadow:0 2px 10px rgba(0,0,0,.12)}
  .page--cover{left:207px;top:71px}
  .page--back{left:662px;top:71px}
  .page--intro{left:207px;top:632px}
  .page--sports{left:662px;top:632px}
  .photo{position:absolute}

  /* Cover */
  .cover-photo{left:0;top:0;width:354px;height:350px;background:linear-gradient(100deg,#b8381c 0%,#e2542b 35%,#7a2a18 55%,#3a2a24 100%)}
  .date-panel{position:absolute;left:213px;top:0;width:124px;height:394px}
  .date-panel__shade{position:absolute;left:0;top:0;width:124px;height:350px;background:rgba(45,40,38,.72)}
  .date-panel__base{position:absolute;left:0;top:350px;width:124px;height:44px;background:var(--panel)}
  .date-panel__text{position:absolute;left:16px;top:0;color:#fff}
  .year-top,.year-bottom{position:absolute;left:0;font-family:"Oswald",sans-serif;font-weight:600;font-size:70px;line-height:1}
  .year-top{top:126px;color:#fff}
  .year-bottom{top:189px;color:var(--orange)}
  .date-rule{position:absolute;left:0;top:258px;width:18px;height:2px;background:#fff}
  .date-range{position:absolute;left:0;top:266px;font-family:"Roboto",sans-serif;font-weight:700;font-size:14.5px;white-space:nowrap}
  .date-month{position:absolute;left:0;top:282px;font-family:"Roboto",sans-serif;font-weight:700;font-size:40px;color:var(--orange);line-height:1.1}
  .date-place{position:absolute;left:0;top:332px;font-family:"Roboto",sans-serif;font-weight:700;font-size:12.5px;white-space:nowrap}
  .date-url{position:absolute;left:0;top:356px;font-size:7px;white-space:nowrap;letter-spacing:.2px}
  .cover-title{position:absolute;left:27px;top:368px}
  .cover-title__year{font-weight:300;font-size:54px;color:var(--orange);line-height:1;letter-spacing:-1px}
  .cover-title__name{margin-top:2px;font-family:"Roboto",sans-serif;font-weight:700;font-size:23px;line-height:21.5px;color:var(--ink)}
  .brand{position:absolute;display:flex;align-items:center;gap:5px;white-space:nowrap;font-weight:600}
  .brand__dot{width:18px;height:18px;border-radius:50%}
  .cover-brand{left:213px;top:461px;font-size:9.5px;color:var(--ink)}
  .cover-brand .brand__dot{background:var(--orange)}

  /* Back */
  .back-photo{left:0;top:0;width:354px;height:384px;background:linear-gradient(180deg,#3c4046 0%,#5a4a48 35%,#a23a2a 55%,#6b6560 78%,#8a8884 100%)}
  .back-title{position:absolute;left:0;top:284px;width:354px;text-align:center;color:#fff}
  .back-title__year{font-weight:300;font-size:38px;color:var(--orange);line-height:1;letter-spacing:1px}
  .back-title__name{margin-top:4px;font-weight:600;font-size:13.5px;letter-spacing:1.6px}
  .back-title__place{margin-top:3px;font-weight:400;font-size:10.5px;letter-spacing:.8px}
  .contact-box{position:absolute;left:32px;top:361px;width:286px;height:101px;background:var(--orange);color:#fff}
  .back-brand{left:13px;top:42px;font-size:8.5px;color:#fff}
  .back-brand .brand__dot{width:16px;height:16px;background:#fff}
  .contact-divider{position:absolute;left:149px;top:32px;width:1.5px;height:42px;background:#fff}
  .contact-list{position:absolute;left:162px;top:30px;list-style:none}
  .contact-list li{display:flex;align-items:center;gap:6px;height:14px;font-size:7px;white-space:nowrap}
  .contact-list li.contact--phone{font-size:9.5px;font-weight:500}
  .contact-list svg{width:11px;height:11px;flex:none}

  /* Intro */
  .intro-band{position:absolute;left:0;top:0;width:354px;height:92px;background:var(--charcoal)}
  .intro-photo{left:27px;top:36px;width:300px;height:196px;border:2px solid var(--orange);border-bottom-color:#ddd;border-left-width:2px;background:linear-gradient(160deg,#e8ecee 0%,#cfd6d2 40%,#c9d94a 60%,#6b8a4a 85%,#3f5a3a 100%)}
  .copy{position:absolute;left:36px;width:282px;color:var(--body)}
  .copy h2{font-size:10.5px;font-weight:700;color:var(--orange);letter-spacing:.1px}
  .copy h2::after{content:"";display:block;width:18px;height:1px;background:var(--ink);margin-top:5px}
  .copy p{font-size:6.6px;line-height:8.6px;text-align:justify;margin-top:8px}
  .copy--games{top:256px}
  .copy--region{top:367px}

  /* Sports */
  .sports-strip{position:absolute;left:0;top:0;width:41px;height:501px;background:var(--charcoal)}
  .sports-frame{position:absolute;left:24px;top:36px;width:308px;height:179px;border-left:2px solid var(--orange);border-bottom:2px solid var(--orange)}
  .sports-photo{left:26px;top:36px;width:306px;height:177px;background:linear-gradient(170deg,#9fb3bf 0%,#c8cfd2 40%,#8d9aa0 60%,#b0642e 75%,#c0703a 100%)}
  .sports-heading{position:absolute;left:56px;top:233px;font-size:9.3px;font-weight:700;color:var(--orange);letter-spacing:.1px}
  .sports-col{position:absolute;top:259px;list-style:none}
  .sports-col li{display:flex;align-items:center;gap:8px;height:17.2px;font-size:7.3px;font-weight:500;color:var(--ink);white-space:nowrap}
  .sports-col li::before{content:"";width:8px;height:8px;border-radius:50%;background:var(--orange);flex:none}
  .sports-col--a{left:56px}
  .sports-col--b{left:164px}
  .sports-col--c{left:256px}
</style>
</head>
<body>
<main class="canvas">

  <section class="page page--cover">
    <div class="photo cover-photo" role="img" aria-label="Photograph of a corridor of red torii gates with inscriptions and a stone path"></div>
    <div class="date-panel">
      <div class="date-panel__shade"></div>
      <div class="date-panel__base"></div>
      <div class="date-panel__text">
        <div class="year-top">20</div>
        <div class="year-bottom">21</div>
        <div class="date-rule"></div>
        <div class="date-range">14TH - 30TH</div>
        <div class="date-month">MAY</div>
        <div class="date-place">KANSAI, JAPAN</div>
        <div class="date-url">www.veteransjourney.com</div>
      </div>
    </div>
    <div class="cover-title">
      <div class="cover-title__year">2021</div>
      <div class="cover-title__name">GLOBAL<br>VETERANS<br>GAMES</div>
    </div>
    <div class="brand cover-brand"><span class="brand__dot"></span>Horizon Travel Bureau</div>
  </section>

  <section class="page page--back">
    <div class="photo back-photo" role="img" aria-label="Photograph of a red Japanese shrine gate building above stone steps with visitors"></div>
    <div class="back-title">
      <div class="back-title__year">2021</div>
      <div class="back-title__name">GLOBAL VETERANS GAMES</div>
      <div class="back-title__place">KANSAI, JAPAN</div>
    </div>
    <div class="contact-box">
      <div class="brand back-brand"><span class="brand__dot"></span>Horizon Travel Bureau</div>
      <div class="contact-divider"></div>
      <ul class="contact-list">
        <li class="contact--phone"><svg viewBox="0 0 12 12"><circle cx="6" cy="6" r="5.3" fill="none" stroke="#fff" stroke-width=".9"/><path d="M4.2 3.4l1 1-.5.7a4 4 0 0 0 2.2 2.2l.7-.5 1 1-.7.8C6 8.5 3.5 6 3.4 4.1z" fill="#fff"/></svg>61 2 5550 1842</li>
        <li><svg viewBox="0 0 12 12"><circle cx="6" cy="6" r="5.3" fill="none" stroke="#fff" stroke-width=".9"/><circle cx="6" cy="6" r="2.8" fill="none" stroke="#fff" stroke-width=".7"/><path d="M3.2 6h5.6M6 3.2v5.6" stroke="#fff" stroke-width=".6"/></svg>www.veteransjourney.com</li>
        <li><svg viewBox="0 0 12 12"><circle cx="6" cy="6" r="5.3" fill="none" stroke="#fff" stroke-width=".9"/><rect x="3.4" y="4.2" width="5.2" height="3.6" fill="none" stroke="#fff" stroke-width=".7"/><path d="M3.4 4.2L6 6.3l2.6-2.1" fill="none" stroke="#fff" stroke-width=".7"/></svg>enquiry@veteransjourney.com</li>
      </ul>
    </div>
  </section>

  <section class="page page--intro">
    <div class="intro-band"></div>
    <div class="photo intro-photo" role="img" aria-label="Photograph of a veteran runner in a yellow race vest stretching his leg on a railing"></div>
    <article class="copy copy--games">
      <h2>THE GLOBAL VETERANS GAMES</h2>
      <p>The 2021 Global Veterans Games will be the 10th Edition of the Games and the first time it will be held in Asia. Since its inception in Toronto in 1985 the Global Veterans Games has grown to become the world's largest mass-participated international sports event.</p>
      <p>The 2021 Games will be held in the Kansai region in the west of Japan and will take place over 17 days from May 14 - 30. An estimated 50,000 participants will meet to play a total of 65 sports and explore this beautiful and alluring country.</p>
    </article>
    <article class="copy copy--region">
      <h2>KANSAI</h2>
      <p>Kansai consists of seven prefectures and was formerly the political and cultural center of Japan for many centuries and includes the cities of Kyoto, Osaka, Nara and Kobe.</p>
      <p>The Kansai region is located in the center of the Japanese islands and is home to over 20 million people. The region is also host to a number of incredible sights including Osaka Castle, Fushimi Inari Shrine, Kinkaku-ji (the Golden Pavilion), Nara Deer Park, Dotonbori District Nishiki Markets and Arashiyama Bamboo Grove.</p>
    </article>
  </section>

  <section class="page page--sports">
    <div class="sports-strip"></div>
    <div class="sports-frame"></div>
    <div class="photo sports-photo" role="img" aria-label="Photograph of a basketball on an indoor court with players in the background"></div>
    <h2 class="sports-heading">THE 2021 SPORTS INCLUDE</h2>
    <ul class="sports-col sports-col--a">
      <li>Archery</li><li>Athletics</li><li>Badminton</li><li>Baseball</li><li>Basketball</li><li>Canoe</li><li>Cycling</li><li>Dance Sports</li><li>Dragonboat</li><li>Football</li><li>Flying Disc (Ultimate)</li><li>Gateball</li>
    </ul>
    <ul class="sports-col sports-col--b">
      <li>Golf</li><li>Handball</li><li>Hockey</li><li>Judo</li><li>Karate</li><li>Lifesaving</li><li>Orienteering</li><li>Rowing</li><li>Rugby</li><li>Sailing</li><li>Shooting</li><li>Softball</li><li>Soft Tennis</li>
    </ul>
    <ul class="sports-col sports-col--c">
      <li>Squash</li><li>Swimming</li><li>Water Polo</li><li>Table Tennis</li><li>Taekwondo</li><li>Tennis</li><li>Tenpin Bowling</li><li>Triathlon</li><li>Tug of War</li><li>Volleyball</li><li>Weightlifting</li>
    </ul>
  </section>

</main>
</body>
</html>
```